Modern & Fresh Sumeray Book Cover

Need a creative e-book cover for my book.

Title: Get Sumeray Sorted
Subtitle: Learn How To Easily Choose & Enroll in the Perfect Coverage at the Perfect Time.

Target Market(s)

60-70 year olds in the United States

Font styles to use
Sans Serif

Colors
9bcb3c
33a6d7

Requirements
Must have
• Must look modern and fresh.
• Use our company colors www.BrovaMint.com

```html
<!DOCTYPE html>
<html lang="en">
<head>
<meta charset="utf-8">
<title>Get Sumeray Sorted</title>
<link href="https://fonts.googleapis.com/css2?family=Jost:ital,wght@0,400;0,500;1,700&display=swap" rel="stylesheet">
<style>
  :root {
    --leaf: #7aab2c;
    --leaf-dark: #3f7a1c;
    --sky: #52acd6;
    --beam: rgba(226, 240, 150, 0.38);
    --paper-edge: #ffffff;
    --spine: #8a8a8a;
    --accent: #d6f545;
    --ink-light: #ffffff;
    --ground: #2f4f1a;
  }
  html, body {
    margin: 0;
    padding: 0;
    overflow: hidden;
  }
  .cover {
    position: relative;
    width: 848px;
    height: 1200px;
    overflow: hidden;
    background: var(--leaf);
    font-family: "Jost", sans-serif;
  }
  .cover-art {
    position: absolute;
    inset: 0;
  }
  .title-block {
    position: absolute;
    right: 48px;
    top: 52px;
    text-align: right;
    color: var(--ink-light);
  }
  .title {
    display: inline-block;
    margin: 0;
    font-weight: 700;
    font-style: italic;
    font-size: 29px;
    line-height: 1;
    padding: 0 2px 8px 0;
    border-bottom: 2px solid var(--ink-light);
    letter-spacing: 0.3px;
  }
  .title-emphasis {
    font-size: 38px;
    margin-left: 6px;
  }
  .subtitle {
    margin: 22px 0 0;
    font-weight: 400;
    font-size: 22.5px;
    line-height: 30px;
  }
  .subtitle-accent {
    color: var(--accent);
  }
  .brand {
    position: absolute;
    left: 20px;
    bottom: 22px;
    display: flex;
    align-items: center;
    gap: 8px;
  }
  .brand-dot {
    width: 12px;
    height: 12px;
    border-radius: 50%;
    background: var(--leaf-dark);
  }
  .brand-name {
    font-weight: 500;
    font-size: 36px;
    line-height: 1;
    color: var(--leaf-dark);
  }
</style>
</head>
<body>
<main class="cover">
  <svg class="cover-art" width="848" height="1200" viewBox="0 0 848 1200" xmlns="http://www.w3.org/2000/svg">
    <defs>
      <radialGradient id="portrait-glow" cx="50%" cy="50%" r="55%">
        <stop offset="0%" stop-color="#a9d3ea"/>
        <stop offset="100%" stop-color="#7dbde0" stop-opacity="0"/>
      </radialGradient>
    </defs>

    <!-- open book pages -->
    <path class="book-pages" fill="var(--sky)"
          d="M0 313 Q230 300 405 381 Q560 345 848 392 L848 1215 Q520 1020 224 1050 Q110 990 0 953 Z"/>
    <path class="page-edge" fill="none" stroke="var(--paper-edge)" stroke-width="2"
          d="M0 313 Q230 300 405 381 Q560 345 848 392"/>
    <path class="page-edge" fill="none" stroke="var(--paper-edge)" stroke-width="2"
          d="M0 953 Q110 990 224 1050 Q520 1020 848 1215"/>
    <line class="book-spine" x1="405" y1="381" x2="224" y2="1050" stroke="var(--spine)" stroke-width="1.5"/>

    <!-- spotlight beam -->
    <polygon class="spotlight" fill="var(--beam)" points="55,0 110,0 848,560 848,1200 560,1200"/>

    <!-- portrait illustration area -->
    <ellipse role="img" aria-label="Line drawing of a smiling older couple in front of a clock face"
             cx="596" cy="650" rx="180" ry="200" fill="url(#portrait-glow)"/>

    <!-- walking figures along the ground -->
    <rect role="img" aria-label="Silhouettes of older people walking, resting and chatting along the ground line"
          x="293" y="1092" width="512" height="98" rx="6" fill="var(--leaf-dark)" opacity="0.55"/>
    <line class="ground-line" x1="220" y1="1190" x2="848" y2="1190" stroke="var(--ground)" stroke-width="1.5"/>
  </svg>

  <header class="title-block">
    <h1 class="title">Get Sumeray <span class="title-emphasis">Sorted</span></h1>
    <p class="subtitle">Learn How To Easily Choose &amp;<br><span class="subtitle-accent">Enroll</span> in the Perfect Coverage at the Perfect Time</p>
  </header>

  <footer class="brand">
    <span class="brand-dot"></span>
    <span class="brand-name">BrovaMint</span>
  </footer>
</main>
</body>
</html>
```